Apartments rental business needs a web for direct reservations.

I need a website that allows my clients to check the property (pictures, a brief description etc) and lets them make reservations. They will be providing the required information such as name, last name, email address and credit card details. Also a calendar where I can update the availability (dates and prices) of the property upon new reservations is a must. I already have a logo that should also be a good starting point for colors, style an inspiration.

Need extra days to review

```html
<!DOCTYPE html>
<html lang="en">
<head>
<meta charset="utf-8">
<title>Coral Cove Bungalows</title>
<link href="https://fonts.googleapis.com/css2?family=Poppins:wght@300;400;500;600&display=swap" rel="stylesheet">
<style>
:root{
  --orange:#f26a2e;
  --orange-dark:#e0531c;
  --teal:#3cbfae;
  --navy:#181d55;
  --hero-blue:#22207a;
  --member-blue:#1c3966;
  --footer:#151a4c;
  --ink:#222;
  --grey:#666;
  --line:#d9d9d9;
  --page:#f3f3f3;
  --white:#fff;
}
*{margin:0;padding:0;box-sizing:border-box}
html,body{width:1200px;height:4190px;overflow:hidden}
body{font-family:'Poppins',sans-serif;color:var(--ink);background:var(--page);position:relative}
section,header,footer{position:absolute;left:0;width:1200px}
.abs{position:absolute}
.accent{color:var(--orange)}
.btn{position:absolute;background:var(--orange);color:var(--white);font-size:12px;display:flex;align-items:center;justify-content:center;border-radius:1px}
.section-title{position:absolute;left:0;width:100%;text-align:center;font-size:26px;font-weight:500}
.divider{position:absolute;left:50%;width:80px;height:10px;transform:translateX(-50%)}
.divider::before,.divider::after{content:"";position:absolute;top:4px;width:32px;height:1px;background:var(--orange)}
.divider::before{left:0}.divider::after{right:0}
.divider span{position:absolute;left:35px;top:0;width:10px;height:10px;border-radius:50%;background:var(--teal)}
.photo{position:absolute}

/* hero */
.hero{top:0;height:530px;overflow:hidden}
.hero-photo{position:absolute;inset:0;background:linear-gradient(160deg,#1a1a1a 0%,#2e2f2a 45%,#3f5360 70%,#5fa7bf 100%)}
.hero-overlay{position:absolute;inset:0}
.brand{position:absolute;left:232px;top:10px;display:flex;align-items:center;gap:6px;color:var(--orange);font-size:11px;font-weight:500;letter-spacing:.5px}
.brand i{width:18px;height:18px;border-radius:50%;background:var(--orange)}
.nav{position:absolute;top:24px;left:0;font-size:12px;color:var(--white)}
.nav a{position:absolute;white-space:nowrap;color:var(--white);text-decoration:none}
.nav a.active{color:var(--orange);border-bottom:1px solid var(--orange);padding-bottom:2px}
.hero-mark{position:absolute;left:236px;top:114px;width:50px;height:50px;border-radius:50%;background:var(--orange)}
.hero-title{position:absolute;left:236px;top:182px;color:var(--white);font-size:35px;font-weight:600;line-height:42px}
.hero-text{position:absolute;left:236px;top:286px;width:370px;color:var(--white);font-size:12.5px;line-height:19px}
.social-rail{position:absolute;left:1170px;top:188px;width:30px;height:153px;background:var(--orange);border-radius:4px 0 0 4px;display:flex;flex-direction:column;align-items:center;justify-content:space-around;padding:6px 0}
.social-rail i{width:10px;height:10px;border-radius:50%;background:var(--white)}

/* search box */
.finder{position:absolute;left:267px;top:452px;width:666px;height:158px;background:var(--white);box-shadow:0 2px 10px rgba(0,0,0,.18)}
.finder h2{position:absolute;top:24px;width:100%;text-align:center;font-size:24px;font-weight:500}
.select{position:absolute;top:93px;height:31px;border:1px solid var(--line);font-size:11px;color:var(--grey);padding:8px 10px}
.select::after{content:"";position:absolute;right:10px;top:10px;width:7px;height:7px;border-right:1px solid #888;border-bottom:1px solid #888;transform:rotate(45deg)}
.select.orange{color:var(--orange);border-color:#f2b59a}
.finder-icon{position:absolute;top:20px;font-size:9px;color:var(--orange);text-align:center}

/* about */
.about{top:610px;height:400px}
.framed{position:absolute;background:var(--white);padding:6px;box-shadow:0 2px 8px rgba(0,0,0,.2)}
.framed div{width:100%;height:100%}
.about-text{position:absolute;left:612px;top:100px;width:355px;text-align:center;font-size:11.5px;line-height:19px;color:var(--grey)}

/* services */
.services{top:1010px;height:406px;overflow:hidden}
.services-bg{position:absolute;inset:0;background:linear-gradient(100deg,#6a5a52 0%,#8b8078 40%,#b6b0aa 70%,#9a9590 100%)}
.services-shade{position:absolute;inset:0;background:rgba(20,20,20,.35)}
.services-text{position:absolute;left:238px;top:110px;width:345px;text-align:center;color:var(--white);font-size:11.5px;line-height:19px}

.stats{top:1416px;height:124px;background:linear-gradient(90deg,#d9531f,#ee7040 50%,#d85a26);color:var(--white)}
.stat{position:absolute;top:28px;width:240px;text-align:center}
.stat b{display:block;font-size:32px;font-weight:500;line-height:40px}
.stat span{font-size:18px}

/* rental */
.rental{top:1540px;height:536px;background:var(--white)}
.tab{position:absolute;top:138px;width:99px;height:28px;color:var(--white);font-size:12px;display:flex;align-items:center;justify-content:center}
.card{position:absolute;top:205px;width:169px;height:222px;background:var(--white);box-shadow:0 1px 6px rgba(0,0,0,.2)}
.card .photo{left:0;top:0;width:169px;height:158px}
.tag{position:absolute;right:4px;top:4px;background:var(--orange);color:var(--white);font-size:8px;padding:1px 6px}
.facts{position:absolute;top:163px;left:4px;right:4px;display:flex;justify-content:space-between;font-size:8.5px;color:var(--grey);line-height:11px}
.facts em{font-style:normal;color:var(--orange)}
.price{position:absolute;left:4px;top:197px;font-size:8.5px;color:var(--grey)}
.price b{color:var(--orange);font-weight:400}
.view{position:absolute;right:6px;top:195px;width:34px;height:14px;border:1px solid var(--line);font-size:8px;text-align:center;line-height:12px;color:var(--grey)}
.view.on{background:var(--orange);color:var(--white);border-color:var(--orange)}

/* book band */
.book{top:2076px;height:144px;background:linear-gradient(90deg,#3fc1ad 0%,#8fc8a3 50%,#fdb784 100%)}
.book h2{position:absolute;top:36px;width:100%;text-align:center;color:var(--white);font-size:31px;font-weight:500;text-shadow:0 1px 3px rgba(0,0,0,.15)}

/* gallery */
.gallery{top:2220px;height:748px;background:var(--white)}
.tile{position:absolute;width:281px;height:237px}
.flat-card{background:var(--white);box-shadow:0 1px 8px rgba(0,0,0,.15)}
.flat-card .inner{position:absolute;inset:14px;border:1px solid var(--orange);text-align:center}
.flat-card h3{margin-top:48px;font-size:14px;font-weight:400;color:var(--orange)}
.flat-card p{margin:12px auto 0;width:150px;font-size:11px;line-height:16px;color:var(--grey)}
.flat-card .view{position:static;display:inline-block;margin-top:10px;width:72px;height:17px;line-height:15px}

/* membership */
.member{top:2968px;height:796px;background:var(--white)}
.member-bg{position:absolute;left:0;top:0;width:1200px;height:577px;background:linear-gradient(180deg,#1c3966,#234a78 60%,#1e416f)}
.member h2{position:absolute;top:34px;width:100%;text-align:center;color:var(--white);font-size:33px;font-weight:500}
.member .lead{position:absolute;top:96px;left:300px;width:600px;text-align:center;color:var(--white);font-size:13px;line-height:21px}
.form-card{position:absolute;left:226px;top:165px;width:750px;height:547px;background:var(--white);box-shadow:0 4px 14px rgba(0,0,0,.25)}
.help{position:absolute;left:0;top:0;width:374px;height:547px;background:var(--teal);color:var(--white);text-align:center}
.help .mark{position:absolute;left:169px;top:68px;width:36px;height:36px;border-radius:50%;background:var(--white)}
.help .name{position:absolute;top:112px;width:100%;font-size:13px;font-weight:500;letter-spacing:1px}
.help h3{position:absolute;top:168px;width:100%;font-size:17px;font-weight:400}
.checks{position:absolute;left:56px;top:228px;list-style:none;text-align:left;font-size:10.5px;line-height:26px}
.checks li::before{content:"✓";margin-right:7px}
.help hr{position:absolute;left:40px;right:40px;top:332px;border:0;border-top:1px solid rgba(255,255,255,.6)}
.help .note{position:absolute;left:46px;top:370px;width:282px;font-size:12.5px;line-height:16px}
.field-label{position:absolute;left:395px;font-size:10.5px;color:var(--orange)}
.input{position:absolute;height:30px;border:1px solid #bbb;font-size:9px;color:#888;padding:9px 10px}
.fine{position:absolute;left:395px;width:332px;font-size:9px;line-height:11px;color:#888}
.fine i{display:inline-block;width:8px;height:8px;border:1px solid #999;margin-right:4px;vertical-align:-1px}

/* footer */
.contact{top:3764px;height:426px;background:var(--footer);color:var(--white)}
.contact h2{position:absolute;top:26px;width:100%;text-align:center;font-size:28px;font-weight:500}
.contact .underline{position:absolute;left:560px;top:68px;width:80px;height:2px;background:var(--orange)}
.quick h4{position:absolute;left:234px;top:92px;color:var(--orange);font-size:16px;font-weight:400}
.quick ul{position:absolute;left:234px;top:130px;list-style:none;font-size:11px;line-height:31.6px}
.quick li{padding-left:10px}
.quick li.on{color:var(--orange);padding-left:0}
.col{position:absolute;top:146px;text-align:center}
.col h5{color:var(--orange);font-size:15px;font-weight:400;margin-top:8px}
.col .rule{height:1px;background:var(--teal);margin-top:8px}
.col svg{display:block;margin:0 auto}
.col p{font-size:10.5px;line-height:14px}
.pay{display:inline-block;width:34px;height:22px;border-radius:3px;background:var(--white)}
.dot{display:inline-block;width:18px;height:18px;border-radius:50%;border:1.5px solid var(--white)}
.copy{position:absolute;bottom:0;left:0;width:1200px;height:28px;background:#10143b;font-size:10px;text-align:center;line-height:28px}
</style>
</head>
<body>

<header class="hero">
  <div class="hero-photo" role="img" aria-label="Bungalow terrace at dusk with lounge chairs and a swimming pool"></div>
  <svg class="hero-overlay" width="1200" height="530" viewBox="0 0 1200 530">
    <polygon points="0,0 488,0 760,460 760,530 0,530" fill="#22207a" fill-opacity=".88"/>
  </svg>
  <div class="brand"><i></i>CORAL COVE</div>
  <nav class="nav">
    <a class="active" style="left:519px">Home</a>
    <a style="left:587px">About Us</a>
    <a style="left:673px">Our Service</a>
    <a style="left:771px">Gallery</a>
    <a style="left:844px">Contact Us</a>
    <svg class="abs" style="left:950px;top:-2px" width="16" height="18" viewBox="0 0 16 18"><circle cx="8" cy="5" r="4" fill="none" stroke="#fff" stroke-width="1.4"/><path d="M1 17c0-4 3-6 7-6s7 2 7 6" fill="none" stroke="#fff" stroke-width="1.4"/></svg>
  </nav>
  <div class="hero-mark"></div>
  <h1 class="hero-title">WelCome To The<br>Coral Cove Bungalows</h1>
  <p class="hero-text">Lorem Ipsum is simply dummy text of the printing and typesetting industry. Lorem Ipsum has been the industry's standard dummy text ever since the 1500s.</p>
  <a class="btn" style="left:236px;top:367px;width:138px;height:35px;font-size:13px">Reserve Now</a>
  <div class="social-rail"><i></i><i></i><i></i><i></i><i></i></div>
</header>

<div class="finder" style="z-index:2">
  <h2>Find Your <span class="accent">Property</span></h2>
  <div class="divider" style="top:63px"><span></span></div>
  <div class="finder-icon" style="left:555px">
    <svg width="18" height="18" viewBox="0 0 18 18"><circle cx="9" cy="6" r="4" fill="none" stroke="#f26a2e" stroke-width="1.3"/><path d="M2 17c0-4 3-6 7-6s7 2 7 6" fill="none" stroke="#f26a2e" stroke-width="1.3"/></svg><br>Login
  </div>
  <svg class="abs" style="left:614px;top:18px" width="20" height="20" viewBox="0 0 20 20"><rect x="1.5" y="3" width="15" height="13" fill="none" stroke="#333" stroke-width="1.3"/><line x1="1.5" y1="7" x2="16.5" y2="7" stroke="#333"/><circle cx="15" cy="15" r="4" fill="#fff" stroke="#333" stroke-width="1.2"/></svg>
  <div class="select" style="left:31px;width:157px">Select Country</div>
  <div class="select orange" style="left:201px;width:156px">Select State</div>
  <div class="select orange" style="left:370px;width:156px">Property Type</div>
  <a class="btn" style="left:539px;top:93px;width:93px;height:31px;font-size:11px">⌕ Search</a>
</div>

<section class="about">
  <div class="framed" style="left:236px;top:39px;width:218px;height:223px"><div role="img" aria-label="White bungalow with a covered porch and red walls" style="background:linear-gradient(180deg,#9cb8d6 0%,#e8e8e4 35%,#b85a35 65%,#6f8b3c 100%)"></div></div>
  <div class="framed" style="left:397px;top:162px;width:192px;height:191px"><div role="img" aria-label="Bungalow side entrance with garden hedges" style="background:linear-gradient(180deg,#c9d9e8 0%,#a7523a 45%,#5e7d38 100%)"></div></div>
  <h2 class="section-title" style="left:590px;width:400px;top:38px">About <span class="accent">Us</span></h2>
  <div class="divider" style="left:790px;top:76px"><span></span></div>
  <p class="about-text">Lorem ipsum is simply dummy text of the printing and typesetting industry. Lorem Ipsum has been the industry's standard dummy text ever since the 1500s, when an unknown printer took a galley of type and scrambled it to make a type specimen book. It has survived not only five centuries, but also the leap into electronic typesetting, remaining essentially unchanged. It was popularised in the 1960s with the release of Lettermill sheets containing Lorem Ipsum passages, and more recently with desktop publishing software like Quillset Layout including versions of Lorem Ipsum.</p>
  <a class="btn" style="left:740px;top:325px;width:101px;height:28px">Read More</a>
</section>

<section class="services">
  <div class="services-bg" role="img" aria-label="Bright living room interior with a sofa and dining table"></div>
  <div class="services-shade"></div>
  <h2 class="section-title" style="left:210px;width:400px;top:48px;color:#fff">Our <span class="accent">Services</span></h2>
  <div class="divider" style="left:410px;top:88px"><span></span></div>
  <p class="services-text">Lorem Ipsum is simply dummy text of the printing and typesetting industry. Lorem Ipsum has been the industry's standard dummy text ever since the 1500s, when an unknown printer took a galley of type and scrambled it to make a type specimen book. It has survived not only five centuries, but also the leap into electronic typesetting, remaining essentially unchanged. It was popularised in the 1960s with the release of Lettermill sheets containing Lorem Ipsum passages, and more recently with desktop publishing software like Quillset Layout including versions of Lorem Ipsum.</p>
  <a class="btn" style="left:359px;top:330px;width:101px;height:28px">Read More</a>
  <div class="framed" style="left:600px;top:50px;width:366px;height:262px"><div role="img" aria-label="Garden lawn with two sun loungers under palm trees" style="background:linear-gradient(180deg,#dfe6de 0%,#4f6a35 45%,#6f9a3a 75%,#8cb14a 100%)"></div></div>
</section>

<section class="stats">
  <div class="stat" style="left:176px"><b>1230+</b><span>New Property</span></div>
  <div class="stat" style="left:483px"><b>930+</b><span>Rented Property</span></div>
  <div class="stat" style="left:786px"><b>4025+</b><span>Happy Client</span></div>
</section>

<section class="rental">
  <h2 class="section-title" style="top:32px">Rental &amp; New <span class="accent">Property</span></h2>
  <div class="divider" style="top:71px"><span></span></div>
  <p class="abs" style="top:90px;width:100%;text-align:center;font-size:13px;color:var(--grey)">Select Your Property Type.</p>
  <a class="tab" style="left:488px;background:var(--orange)">For Rent</a>
  <a class="tab" style="left:613px;background:var(--teal)">For Sale</a>

  <div class="card" style="left:234px">
    <div class="photo" role="img" aria-label="Modern white kitchen" style="background:linear-gradient(180deg,#e3e4e2,#a9aaa6 60%,#3b3b3b)"></div>
    <span class="tag">Rent</span>
    <div class="facts"><span>Bedrooms<br><em>2</em></span><span>Bathrooms<br><em>2</em></span><span>Super area<br><em>610 sqft</em></span></div>
    <div class="price"><b>Rent</b> &nbsp;250$ Per Month</div><div class="view">View</div>
  </div>
  <div class="card" style="left:421px">
    <div class="photo" role="img" aria-label="Living room with grey sofa and red cushions" style="background:linear-gradient(180deg,#e4e1da,#c9c3b8 55%,#53575a 80%,#b74a3a)"></div>
    <span class="tag">Rent</span>
    <div class="facts"><span>Bedrooms<br><em>2</em></span><span>Bathrooms<br><em>2</em></span><span>Super area<br><em>610 sqft</em></span></div>
    <div class="price"><b>Rent</b> &nbsp;250$ Per Month</div><div class="view on">View</div>
  </div>
  <div class="card" style="left:608px">
    <div class="photo" role="img" aria-label="Bedroom with white bed and blue towels" style="background:linear-gradient(180deg,#b8b2a8,#d8d3cb 55%,#f2f2f2 80%,#2c3f7a)"></div>
    <span class="tag">Rent</span>
    <div class="facts"><span>Bedrooms<br><em>2</em></span><span>Bathrooms<br><em>2</em></span><span>Super area<br><em>610 sqft</em></span></div>
    <div class="price"><b>Rent</b> &nbsp;250$ Per Month</div><div class="view">View</div>
  </div>
  <div class="card" style="left:795px">
    <div class="photo" role="img" aria-label="Bathroom with wall-mounted water heater" style="background:linear-gradient(180deg,#c4d2d7,#e8ecea 50%,#8fa5ad)"></div>
    <span class="tag">Rent</span>
    <div class="facts"><span>Bedrooms<br><em>2</em></span><span>Bathrooms<br><em>2</em></span><span>Super area<br><em>610 sqft</em></span></div>
    <div class="price"><b>Rent</b> &nbsp;250$ Per Month</div><div class="view">View</div>
  </div>
  <a class="btn" style="left:550px;top:468px;width:101px;height:28px;font-size:12.5px">View More</a>
</section>

<section class="book">
  <h2>Book &nbsp;Your Suitable Property</h2>
  <a class="btn" style="left:538px;top:93px;width:124px;height:28px;font-weight:500">Reserve Now</a>
</section>

<section class="gallery">
  <h2 class="section-title" style="top:44px">Property <span class="accent">Gallery</span></h2>
  <div class="divider" style="top:83px"><span></span></div>
  <div class="tile" style="left:10px;top:136px;background:linear-gradient(180deg,#8fb7e0 0%,#e9ecef 40%,#b9b6ae 80%,#7a8a5a)" role="img" aria-label="Modern white villa with glass balconies"></div>
  <div class="tile" style="left:309px;top:136px;background:linear-gradient(180deg,#4a7bb5 0%,#d38a3a 35%,#5b6a3a 65%,#6e5e4a)" role="img" aria-label="Wooden cottage among autumn trees"></div>
  <div class="tile flat-card" style="left:610px;top:136px">
    <div class="inner"><h3>2 BHK FLAT</h3><p>Lorem Ipsum is simply dummy text of the printing and typesetting industry..</p><span class="view">View Details</span></div>
  </div>
  <div class="tile" style="left:909px;top:136px;background:linear-gradient(180deg,#a2743f 0%,#e6dccb 45%,#cfc7b8 75%,#5d4b37)" role="img" aria-label="Open living room with white sofas and wooden gallery"></div>
  <div class="tile" style="left:10px;top:393px;background:linear-gradient(180deg,#f1eee8 0%,#d8d1c6 50%,#5b4432 80%,#9a8a74)" role="img" aria-label="Dining room with chandelier"></div>
  <div class="tile" style="left:309px;top:393px;background:linear-gradient(180deg,#f3f1ee 0%,#e7c9cc 45%,#d9b4b8 70%,#5d7a3a)" role="img" aria-label="Pastel townhouse facade with balconies"></div>
  <div class="tile" style="left:610px;top:393px;background:linear-gradient(180deg,#e8ecef 0%,#8a8f94 40%,#a8abac 70%,#6d9a3b)" role="img" aria-label="Grey two-storey house with a front lawn"></div>
  <div class="tile" style="left:909px;top:393px;background:linear-gradient(180deg,#2f3a4a 0%,#a0703a 45%,#3a3230 75%,#6e4a2c)" role="img" aria-label="Living room with fireplace and dark sofa"></div>
  <a class="btn" style="left:550px;top:674px;width:101px;height:28px;font-size:12.5px">View More</a>
</section>

<section class="member">
  <div class="member-bg"></div>
  <h2>Contact For Membership</h2>
  <p class="lead">We'd love to talk about how we can work together. Please fill out the form and we'll be in touch shortly</p>
  <div class="form-card">
    <div class="help">
      <div class="mark"></div>
      <div class="name">CORAL COVE</div>
      <h3>We're here to help you</h3>
      <ul class="checks">
        <li>Lorem Ipsum is simply dummy text of the printing</li>
        <li>Lorem Ipsum is simply dummy text of the printing</li>
        <li>Lorem Ipsum is simply dummy text of the printing</li>
      </ul>
      <hr>
      <p class="note">Lorem Ipsum is simply dummy text of the printing and typesetting industry. Lorem Ipsum has been the industry's standard dummy text ever since the 1500s.</p>
    </div>
    <span class="field-label" style="top:26px">Name *</span>
    <div class="input" style="left:395px;top:46px;width:158px">First name</div>
    <div class="input" style="left:569px;top:46px;width:158px">Last name</div>
    <span class="field-label" style="top:89px">Card Details</span>
    <div class="input" style="left:395px;top:111px;width:332px">Enter Your card details &nbsp;&nbsp;CVV &nbsp;// Card Number</div>
    <span class="field-label" style="top:162px">Email *</span>
    <div class="input" style="left:395px;top:184px;width:332px">you@coralcove.com</div>
    <span class="field-label" style="top:231px">Country *</span>
    <div class="input" style="left:395px;top:254px;width:332px">Select country</div>
    <span class="field-label" style="top:302px">Type your message</span>
    <div class="input" style="left:395px;top:324px;width:332px;height:63px">Tell us more about your Property</div>
    <p class="fine" style="top:404px"><i></i>Yes, I'd like to receive marketing communications regarding Coral Cove Bungalows products, services, and events. I can unsubscribe at any time.</p>
    <p class="fine" style="top:449px">By clicking the submit button, you agree to allow Coral Cove Bungalows to store and process the information above for contact purposes. Please read our Privacy Policy.</p>
    <a class="btn" style="left:517px;top:498px;width:90px;height:29px">Submit</a>
  </div>
</section>

<footer class="contact">
  <h2>Contact Us</h2>
  <div class="underline"></div>
  <div class="quick">
    <h4>Quick Links</h4>
    <ul>
      <li class="on">› Home</li><li>About Us</li><li>Our Services</li><li>Property Details</li>
      <li>Property Gallery</li><li>Customer Support</li><li>Privacy &amp; Policy</li><li>Contact Us</li>
    </ul>
  </div>
  <div class="col" style="left:384px;width:196px;top:140px">
    <svg width="38" height="34" viewBox="0 0 38 34"><rect x="10" y="2" width="24" height="17" fill="none" stroke="#fff" stroke-width="1.4"/><path d="M10 2l12 9 12-9" fill="none" stroke="#fff" stroke-width="1.4"/><path d="M4 16c2-2 4-2 5 0l2 3c1 2-1 3-2 4 2 3 4 5 7 7 1-1 2-3 4-2l3 2c2 1 2 3 0 5-3 3-9 0-14-5S1 19 4 16z" fill="none" stroke="#fff" stroke-width="1.3"/></svg>
    <h5>Contact Us</h5><div class="rule"></div>
    <p style="margin-top:12px"><span class="accent">✆</span> +1 555 0142</p>
    <p style="margin-top:14px"><span class="accent">✉</span> www.CoralCoveBungalows.com</p>
    <div style="margin-top:20px;display:flex;gap:12px;justify-content:center"><span class="dot"></span><span class="dot"></span><span class="dot"></span><span class="dot"></span><span class="dot"></span></div>
  </div>
  <div class="col" style="left:592px;width:162px;top:140px">
    <svg width="40" height="34" viewBox="0 0 40 34"><path d="M2 16L38 2 30 32 18 22z M18 22l20-20 M18 22v10l5-6" fill="none" stroke="#fff" stroke-width="1.4" stroke-linejoin="round"/></svg>
    <h5>Newsletter</h5><div class="rule"></div>
    <p style="margin-top:12px;font-size:9.5px;line-height:12px">Subscribe to our Newsletter and stay up to date with all event coming straight in your mailbox</p>
    <div style="margin:12px auto 0;width:155px;height:22px;background:#fff;color:#666;font-size:9px;text-align:left;padding:5px 6px">Email</div>
    <div style="margin:12px auto 0;width:74px;height:20px;background:var(--orange);font-size:9px;line-height:20px">Subscribe</div>
  </div>
  <div class="col" style="left:790px;width:174px;top:140px">
    <svg width="44" height="34" viewBox="0 0 44 34"><rect x="2" y="10" width="28" height="20" fill="none" stroke="#fff" stroke-width="1.4"/><path d="M2 10l14 11 14-11" fill="none" stroke="#fff" stroke-width="1.4"/><circle cx="32" cy="10" r="8" fill="#151a4c" stroke="#fff" stroke-width="1.4"/><path d="M32 5v10M29 8h5M29 12h5" stroke="#fff" stroke-width="1.2"/></svg>
    <h5>Payment Option</h5><div class="rule"></div>
    <div style="margin-top:12px;display:flex;gap:14px;justify-content:center"><span class="pay"></span><span class="pay"></span><span class="pay"></span></div>
    <div style="margin-top:12px;display:flex;gap:14px;justify-content:center"><span class="pay"></span><span class="pay"></span><span class="pay"></span></div>
  </div>
  <div class="copy">© Coral Cove Bungalows. All rights reserved.</div>
</footer>

</body>
</html>
```